a residential painting contractor I need a 6x9 postcard made

I already have a logo, I'm trying to offer my services to people. you can put that there's a 250$ discount for first time customers. include my License number #4627381 as well as the services I offer, interior and exterior painting, pressure washing, cabinet painting, epoxy floors, wood staining, decks, fences and much more. I'm licensed bonded and insured as well.

Target Market(s)

residential consumers (homeowners)

Industry/Entity Type

Painting contractor

Requirements
Must have
• postage stuff on the back I've linked some pictures top right please, my license number, what I do, phone number (555)317-0846 email velbrushworks7@mailzo.net, front and back of postcard
Nice to have
• well lit house in the background, maybe little circles of people doing some of the services I offer

```html
<!DOCTYPE html>
<html lang="en">
<head>
<meta charset="utf-8">
<title>Velbrush Works – Postcard Front and Back</title>
<link rel="stylesheet" href="https://fonts.googleapis.com/css2?family=Barlow+Condensed:wght@700&family=Work+Sans:wght@500;600;700&display=swap">
<style>
  :root {
    --page: #e4e5e7;
    --sky: #c4e5f0;
    --sky-light: #dcf0f6;
    --ink: #1d1c21;
    --blob: #2b2930;
    --blob-grey: #a9abb0;
    --white: #ffffff;
    --ring: #2e2b3b;
  }
  * { box-sizing: border-box; margin: 0; padding: 0; }
  html, body { width: 1200px; height: 470px; overflow: hidden; }
  body {
    background: var(--page);
    font-family: "Work Sans", Arial, sans-serif;
    color: var(--ink);
    position: relative;
  }
  .card {
    position: absolute;
    top: 63px;
    width: 516px;
    height: 344px;
    overflow: hidden;
    box-shadow: 3px 4px 8px rgba(0,0,0,.25);
  }
  .card--front { left: 64px; background: linear-gradient(90deg, var(--sky-light), var(--sky) 45%, #cde9f3); }
  .card--back { left: 620px; background: var(--white); }
  .abs { position: absolute; }

  /* front */
  .front__wall {
    left: 0; top: 0; width: 170px; height: 344px;
    background: linear-gradient(90deg, #f7f8f8 0%, #eef3f4 55%, rgba(220,240,246,0) 100%);
  }
  .front__roller {
    left: 40px; top: 215px; width: 130px; height: 129px;
    background: radial-gradient(ellipse at 45% 45%, #e6e8e9, #d7dfe2 55%, rgba(215,223,226,0) 75%);
  }
  .front__band {
    left: 0; top: 44px; width: 365px; height: 87px;
    background: var(--ink);
    clip-path: polygon(0 0, 100% 0, 94% 100%, 0 100%);
  }
  .front__headline {
    left: 34px; top: 50px;
    font-family: "Barlow Condensed", "Arial Narrow", sans-serif;
    font-weight: 700; font-size: 40px; line-height: 40px;
    color: var(--white); letter-spacing: .3px;
  }
  .brand {
    left: 360px; top: 20px; width: 140px; height: 140px;
    display: flex; flex-direction: column; align-items: center; justify-content: center; gap: 10px;
  }
  .brand__dot { width: 50px; height: 50px; border-radius: 50%; background: var(--ink); }
  .brand__name { font-weight: 700; font-size: 18px; line-height: 20px; text-align: center; color: var(--ink); }
  .services { list-style: none; }
  .services li { display: flex; align-items: center; white-space: nowrap; }
  .tick { width: 19px; height: 19px; margin-right: 6px; flex: none; }
  .tick--inline { margin-left: 6px; }
  .front__services {
    left: 33px; top: 135px;
    font-weight: 500; font-size: 14.5px; line-height: 19px;
  }
  .front__services li { height: 22px; }
  .offer { left: 182px; top: 196px; width: 180px; height: 145px; }
  .offer__text { left: 200px; top: 235px; width: 150px; color: var(--white); text-align: center; transform: rotate(-7deg); }
  .offer__label { font-weight: 600; font-size: 15px; line-height: 16px; padding-left: 40px; }
  .offer__amount { font-weight: 700; font-size: 43px; line-height: 44px; letter-spacing: -1px; }
  .offer__note { font-weight: 600; font-size: 11.5px; line-height: 12px; padding-left: 14px; }
  .front__info { right: 22px; text-align: right; font-weight: 500; }
  .front__rule { height: 1.5px; background: var(--ink); right: 0; }
  .front__cred { top: 224px; font-size: 11.5px; line-height: 15px; }
  .front__license { top: 263px; font-size: 11.5px; line-height: 14.5px; }
  .front__phone { top: 294px; font-size: 16.5px; line-height: 20px; }
  .front__email { top: 313px; font-size: 11px; line-height: 14px; }

  /* back */
  .back__scene {
    left: 0; top: 0; width: 370px; height: 344px;
    clip-path: polygon(0 0, 100% 0, 56% 100%, 0 100%);
    background: linear-gradient(160deg, #bfe0ee 0%, #d8ecf3 45%, #c8dfe7 75%, #b9ccd4 100%);
  }
  .back__title { left: 29px; top: 38px; font-weight: 600; font-size: 21px; line-height: 27px; }
  .back__services { left: 29px; top: 96px; font-weight: 500; font-size: 15px; line-height: 19px; }
  .back__services .tick { width: 15px; height: 15px; margin-right: 6px; }
  .back__services .tick--inline { margin-left: 4px; }
  .back__more { left: 29px; top: 188px; font-weight: 500; font-size: 15px; line-height: 19px; }
  .back__cred {
    left: 28px; top: 218px; width: 173px; height: 44px;
    border: 1px solid var(--ink); border-top-right-radius: 22px;
    font-weight: 500; font-size: 15px; line-height: 19px; padding: 3px 0 0 10px;
  }
  .back__contact { left: 29px; font-weight: 500; font-size: 13px; line-height: 16px; display: flex; align-items: center; gap: 5px; }
  .back__contact svg { width: 13px; height: 13px; }
  .photo { border-radius: 50%; border: 3px solid var(--ring); }
  .photo--wood { left: 296px; top: 25px; width: 82px; height: 82px; background: linear-gradient(135deg, #d9b27a, #9a6a34 55%, #5b3a1b); }
  .photo--wash { left: 222px; top: 84px; width: 138px; height: 138px; background: linear-gradient(150deg, #b9ad9a, #8f8676 50%, #a7a294); }
  .photo--epoxy { left: 214px; top: 201px; width: 81px; height: 81px; background: linear-gradient(160deg, #a57a52, #5d7f8f 50%, #294b5e); }
  .postage {
    left: 411px; top: 28px; width: 90px; height: 66px;
    border: 1px solid #555; text-align: center;
    font-weight: 700; font-size: 10px; line-height: 12.5px; padding-top: 2px;
  }
  .postage__paid { font-size: 12px; line-height: 14px; }
  .addressee {
    left: 390px; top: 107px; width: 111px; height: 27px;
    border: 1px solid var(--ink); font-weight: 600; font-size: 7.3px; line-height: 9px; padding: 3px 0 0 8px;
  }
  .address-line { left: 331px; width: 170px; height: 1px; background: var(--ink); }
</style>
</head>
<body>
<svg width="0" height="0" style="position:absolute">
  <defs>
    <symbol id="tick" viewBox="0 0 24 24">
      <path d="M19.5 8.5A9 9 0 1 1 15.5 3.6" fill="none" stroke="currentColor" stroke-width="2.4" stroke-linecap="round"/>
      <path d="M7 11.5l4.5 4.5L22 4" fill="none" stroke="currentColor" stroke-width="2.8" stroke-linecap="round" stroke-linejoin="round"/>
    </symbol>
  </defs>
</svg>

<section class="card card--front" aria-label="Postcard front">
  <div class="abs front__wall" role="img" aria-label="White painted wall"></div>
  <div class="abs front__roller" role="img" aria-label="Gloved hand rolling white paint"></div>
  <div class="abs front__band"></div>
  <h1 class="abs front__headline">INTERIOR AND<br>EXTERIOR PAINTING</h1>
  <div class="abs brand">
    <span class="brand__dot"></span>
    <span class="brand__name">VELBRUSH<br>WORKS</span>
  </div>
  <ul class="abs services front__services">
    <li><svg class="tick"><use href="#tick"/></svg>Pressure Washing<svg class="tick tick--inline"><use href="#tick"/></svg>Cabinet Painting</li>
    <li><svg class="tick"><use href="#tick"/></svg>Epoxy Floors<svg class="tick tick--inline"><use href="#tick"/></svg>Wood Staining</li>
    <li><svg class="tick"><use href="#tick"/></svg>Decks<svg class="tick tick--inline"><use href="#tick"/></svg>Fences And Much More</li>
  </ul>
  <svg class="abs offer" viewBox="0 0 180 145">
    <path d="M60 22C85 2 130 0 150 6c22 7 30 40 18 70-10 25-40 20-60 10Z" fill="var(--blob-grey)"/>
    <path d="M30 34C60 14 110 14 140 26c25 10 26 50 14 76-14 30-60 38-100 34C20 132 4 110 6 80 8 58 14 45 30 34Z" fill="var(--blob)"/>
  </svg>
  <div class="abs offer__text">
    <div class="offer__label">discount</div>
    <div class="offer__amount">$250</div>
    <div class="offer__note">for first time<br>customers</div>
  </div>
  <p class="abs front__info front__cred">I'm licensed bonded<br>and insured as well.</p>
  <div class="abs front__rule" style="top:257px;left:363px"></div>
  <p class="abs front__info front__license">License number<br>#4627381</p>
  <div class="abs front__rule" style="top:290px;left:348px"></div>
  <p class="abs front__info front__phone">(555)317-0846</p>
  <p class="abs front__info front__email">velbrushworks7@mailzo.net</p>
</section>

<section class="card card--back" aria-label="Postcard back">
  <div class="abs back__scene" role="img" aria-label="Faded house under a blue sky"></div>
  <h2 class="abs back__title">Interior And<br>Exterior Painting</h2>
  <ul class="abs services back__services">
    <li><svg class="tick"><use href="#tick"/></svg>pressure washing</li>
    <li><svg class="tick"><use href="#tick"/></svg>cabinet painting</li>
    <li><svg class="tick"><use href="#tick"/></svg>epoxy floors</li>
    <li><svg class="tick"><use href="#tick"/></svg>wood staining</li>
    <li><svg class="tick"><use href="#tick"/></svg>decks<svg class="tick tick--inline"><use href="#tick"/></svg>fences</li>
  </ul>
  <p class="abs back__more">and much more</p>
  <p class="abs back__cred">I'm licensed bonded<br>and insured as well.</p>
  <p class="abs back__contact" style="top:271px">
    <svg viewBox="0 0 24 24"><path d="M6 3l3 4-2 2c1 3 4 6 7 7l2-2 4 3-2 3C11 20 4 13 3 5Z" fill="none" stroke="currentColor" stroke-width="1.8" stroke-linejoin="round"/></svg>(555)317-0846
  </p>
  <p class="abs back__contact" style="top:289px">
    <svg viewBox="0 0 24 24"><rect x="2" y="5" width="20" height="14" fill="none" stroke="currentColor" stroke-width="1.8"/><path d="M2 5l10 8 10-8" fill="none" stroke="currentColor" stroke-width="1.8"/></svg>velbrushworks7@mailzo.net
  </p>
  <div class="abs photo photo--wood" role="img" aria-label="Brush staining a wooden deck board"></div>
  <div class="abs photo photo--wash" role="img" aria-label="Pressure washing paving stones"></div>
  <div class="abs photo photo--epoxy" role="img" aria-label="Glossy epoxy floor being poured"></div>
  <div class="abs postage">PRSRT STD<br>ECRWSS<br>U.S.POSTAGE<br><span class="postage__paid">PAID</span><br>EDDM Retail</div>
  <div class="abs addressee">LOCAL POSTAL<br>CUSTOMER</div>
  <div class="abs address-line" style="top:224px"></div>
  <div class="abs address-line" style="top:265px"></div>
  <div class="abs address-line" style="top:305px"></div>
</section>
</body>
</html>
```